Substance abuse awareness flyer for school age kids

I am needing a flyer for school-age kids. What if it were designed to look like an Voxtab with someone texting and the text bubbles were some of the text below with emojis? Maybe a text chain between to friends:

Maybe the first text bubble says "I'm thinking about using drugs and alcohol"
the next bubble: "Just say no!" ( perhaps a stop sign emoji ?)

"Talk to your parents, your teachers at school, or your doctor about how drugs and alcohol can harm you"

another text bubble "did you know that alcohol and drugs could lead to..."
then include some of the info below (see links for more info).
Where ever you get info, it must be cited.

this needs to be English on one side and Spanish on the other side and needs to include the logo attached.

The effects of substance abuse
BHW: https://www.bhwagency.org/youth/features/teen-substance-use.html
Affect growth and development, especially brain development. Not able to focus at school or be around friends. https://www.kestrowline.org/sites/default/files/preventingdruguse_2.pdf
Leads to risky behaviors and lack of impulse control (dangerous activities) https://www.kestrowline.org/sites/default/files/preventingdruguse_2.pdf
Contribute to health problems as an adult: heart disease, high blood pressure, and trouble sleeping.

Target Market(s)

school age kids 9-20

Requirements
Must have
• Print ready: 8.5x11

```html
<!DOCTYPE html>
<html lang="en">
<head>
<meta charset="utf-8">
<title>Substance Abuse Awareness Flyer</title>
<link rel="stylesheet" href="https://fonts.googleapis.com/css2?family=Arimo:wght@400;700&display=swap">
<style>
  :root {
    --frame-blue: #1fb5e4;
    --panel-white: #ffffff;
    --line-blue: #b9e2f4;
    --scene-top: #c9def4;
    --scene-bottom: #f3b588;
    --bubble-grey: #e6e6e6;
    --bubble-blue: #1e88f0;
    --bubble-shadow: rgba(20, 40, 80, 0.18);
    --ink-dark: #1a1a1a;
    --ink-light: #ffffff;
    --tick-green: #2fb34a;
    --curl: #dde3ea;
    --seal-ink: #2a4a8a;
  }
  * { box-sizing: border-box; margin: 0; padding: 0; }
  html, body { width: 883px; height: 1200px; overflow: hidden; }
  body { font-family: "Arimo", Arial, sans-serif; background: var(--frame-blue); }

  .flyer { position: relative; width: 883px; height: 1200px; background: var(--frame-blue); }

  .panel {
    position: absolute; left: 33px; top: 29px; width: 820px; height: 1060px;
    background: var(--panel-white); overflow: hidden;
  }
  .panel-art { position: absolute; inset: 0; }

  .bubble {
    position: absolute; border-radius: 18px;
    box-shadow: 8px 8px 0 var(--bubble-shadow);
    font-size: 21px; line-height: 1.27;
  }
  .bubble--incoming { background: var(--bubble-grey); color: var(--ink-dark); }
  .bubble--outgoing { background: var(--bubble-blue); color: var(--ink-light); }

  .bubble-question { left: 57px; top: 82px; width: 360px; height: 72px; padding: 9px 22px; }
  .bubble-refusal { left: 444px; top: 169px; width: 322px; height: 50px; padding: 12px 20px 0; text-align: center; }
  .bubble-advice { left: 354px; top: 242px; width: 379px; height: 134px; padding: 14px 22px 0 24px; font-size: 21.5px; }
  .bubble-facts { left: 264px; top: 402px; width: 469px; height: 448px; padding: 14px 40px 0 26px; }

  .facts-intro { margin-bottom: 12px; }
  .facts-list { list-style: none; }
  .fact { display: flex; gap: 10px; font-weight: 700; font-size: 21px; line-height: 1.27; margin-bottom: 26px; }
  .fact:last-child { margin-bottom: 0; }
  .fact-tick {
    flex: 0 0 22px; height: 22px; margin-top: 2px; border-radius: 4px;
    background: var(--tick-green); display: flex; align-items: center; justify-content: center;
  }
  sup { font-size: 0.55em; line-height: 0; }

  .references {
    position: absolute; left: 33px; top: 1117px; width: 650px;
    color: var(--ink-light); font-size: 12.5px; line-height: 1.5;
  }

  .seal {
    position: absolute; left: 724px; top: 1052px; width: 140px; height: 140px;
    border-radius: 50%; background: var(--panel-white);
    display: flex; align-items: center; justify-content: center; text-align: center;
    border: 4px solid var(--frame-blue); box-shadow: 0 0 0 3px var(--panel-white);
  }
  .seal-name { font-weight: 700; font-size: 15px; line-height: 1.15; color: var(--seal-ink); width: 96px; }
</style>
</head>
<body>
<main class="flyer">
  <section class="panel">
    <svg class="panel-art" width="820" height="1060" viewBox="0 0 820 1060">
      <defs>
        <linearGradient id="sceneFill" x1="0.8" y1="0" x2="0.1" y2="1">
          <stop offset="0" stop-color="var(--scene-top)"/>
          <stop offset="1" stop-color="var(--scene-bottom)"/>
        </linearGradient>
      </defs>
      <circle cx="722" cy="28" r="50" fill="none" stroke="var(--line-blue)" stroke-width="6"/>
      <circle cx="672" cy="34" r="14" fill="none" stroke="var(--line-blue)" stroke-width="4"/>
      <path d="M692 82 v30 M677 97 h30" stroke="var(--line-blue)" stroke-width="5"/>
      <path d="M790 180 v30 M775 195 h30" stroke="var(--line-blue)" stroke-width="5"/>
      <rect role="img" aria-label="Illustration: a hand holding a smartphone showing a text chat" x="0" y="50" width="600" height="1010" rx="48" fill="url(#sceneFill)"/>
      <path d="M820 900 C 760 950 720 1005 690 1060 L 820 1060 Z" fill="var(--curl)"/>
    </svg>

    <div class="bubble bubble--incoming bubble-question">I’m thinking about using drugs and alcohol 🤔🤔🤔</div>
    <div class="bubble bubble--outgoing bubble-refusal">JUST SAY NO!!! ⛔⛔✋</div>
    <div class="bubble bubble--outgoing bubble-advice">Talk to your PARENTS, your TEACHER at school, or your DOCTOR about how <strong>drugs</strong> and <strong>alcohol</strong> can harm you.</div>
    <div class="bubble bubble--outgoing bubble-facts">
      <p class="facts-intro">Did you know that alcohol and drugs could lead to...⚠️⚠️⚠️</p>
      <ul class="facts-list">
        <li class="fact"><span class="fact-tick"><svg width="16" height="16" viewBox="0 0 16 16"><path d="M3 8.5l3 3 7-7" fill="none" stroke="#fff" stroke-width="2.6"/></svg></span><span>Affect growth and development, especially brain development<sup>[1]</sup></span></li>
        <li class="fact"><span class="fact-tick"><svg width="16" height="16" viewBox="0 0 16 16"><path d="M3 8.5l3 3 7-7" fill="none" stroke="#fff" stroke-width="2.6"/></svg></span><span>Not able to focus at school or be around friends<sup>[1]</sup></span></li>
        <li class="fact"><span class="fact-tick"><svg width="16" height="16" viewBox="0 0 16 16"><path d="M3 8.5l3 3 7-7" fill="none" stroke="#fff" stroke-width="2.6"/></svg></span><span>Leads to risky behaviors and lack of impulse control (dangerous activities)<sup>[2]</sup></span></li>
        <li class="fact"><span class="fact-tick"><svg width="16" height="16" viewBox="0 0 16 16"><path d="M3 8.5l3 3 7-7" fill="none" stroke="#fff" stroke-width="2.6"/></svg></span><span>Contribute to health problems as an adult: heart disease, high blood pressure, and trouble sleeping<sup>[3]</sup></span></li>
      </ul>
    </div>
  </section>

  <footer class="references">
    <p>[1] https://www.bhwagency.org/youth/features/teen-substance-use.html</p>
    <p>[2] https://www.kestrowline.org/sites/default/files/preventingdruguse_2.pdf</p>
    <p>[3] https://www.kestrowline.org/sites/default/files/preventingdruguse_2.pdf</p>
  </footer>

  <div class="seal"><span class="seal-name">Rivermark Health</span></div>
</main>
</body>
</html>
```